Lantern - Web Design Project

We are seeking to have our website redesigned. Our current webpage is rather dated looking www.lantern-outcomes.com We will be utilizing similar content to explain our services as what is in the website now. We do not see it at a retail portal but rather a website for those inquiring about our services as a reference check so to speak.

We wish to have a look that is considered clean, fresh, contemporary and contains a business savvy vibe.

We prefer isolated white background and also wish to retain the integrity of our Logo and colour scheme.

We are looking for something that doesnt look like it was designed at home on sitemoose. We are hoping to find something that looks like it would reside on a tablet.
Updates

Hello designers!

We apologize for our tardiness as we have been quite preoccupied. We will be extending our invites to the end of January!

Hello All,

Please review our offer once again for updated requirements.  We are hoping to accept a design by months end.

Lantern

Target Market(s)

Business to business clients and Large manufacturers

Industry/Entity Type

Retail

Requirements
Must have
• Existing Logo

There must be an area dedicated to an intro video that will be incorporated on our landing page.

We require design of the other pages as well not only the landing page.

```html
<!DOCTYPE html>
<html lang="en">
<head>
<meta charset="utf-8">
<title>Lantern Performance Group</title>
<link href="https://fonts.googleapis.com/css2?family=Lato:wght@400;700&family=Roboto+Condensed:wght@700&display=swap" rel="stylesheet">
<style>
:root{
  --red:#e8262a;
  --ink:#3a3a3a;
  --line:#c9c9c9;
  --dark:#222222;
  --white:#ffffff;
  --chip:#e6e6e6;
  --social:#a9a9a9;
  --hero-top:#262a33;
  --hero-bottom:#3b352b;
}
*{box-sizing:border-box;margin:0;padding:0}
html,body{width:1200px;height:913px;overflow:hidden;background:var(--white)}
body{font-family:"Lato",Arial,sans-serif;color:var(--ink);position:relative}
.abs{position:absolute}
.brand{left:132px;top:22px;display:flex;align-items:center;gap:10px}
.brand-dot{width:22px;height:22px;border-radius:50%;background:var(--red)}
.brand-name{font-size:48px;font-weight:400;color:#555;letter-spacing:-1px;line-height:1}
.contact-bar{top:20px;left:606px;display:flex;align-items:center;font-size:14px;color:var(--ink)}
.contact-bar span{display:flex;align-items:center;gap:8px;margin-right:22px}
.lang{top:19px;left:954px;display:flex;gap:3px;font-size:12.5px}
.lang span{display:block;height:20px;line-height:20px;padding:0 6px;background:var(--chip);color:#555}
.lang .active{color:var(--red)}
.lang .signin{background:var(--red);color:var(--white);padding:0 9px;margin-left:1px}
.search{left:854px;top:54px;width:214px;height:28px;border:1px solid var(--line);font-size:12.5px;color:#777;padding:6px 10px}
.search svg{position:absolute;right:5px;top:5px}
.nav{left:132px;top:103px;width:936px;height:40px;border-top:1px solid var(--red);border-bottom:1px solid var(--red);font-size:14.5px;text-transform:uppercase;color:var(--ink)}
.nav a{position:absolute;top:0;color:inherit;text-decoration:none;height:100%;display:flex;align-items:center;white-space:nowrap}
.nav .home{left:0;background:var(--red);color:var(--white);width:96px;justify-content:center}
.nav .who{left:120px}
.nav .cross{left:256px}
.nav .perf{left:437px}
.nav .sustain{left:667px}
.nav .join{left:853px}
.hero{left:132px;top:151px;width:936px;height:404px;background:linear-gradient(180deg,var(--hero-top) 0%,var(--hero-bottom) 100%)}
.quote{left:168px;top:200px;font-family:"Roboto Condensed","Arial Narrow",sans-serif;font-weight:700;font-size:22px;line-height:26px;color:var(--white)}
.quote cite{display:block;color:var(--red);font-style:normal;margin-top:4px}
.dots{left:996px;top:531px;display:flex;gap:2px}
.dots i{width:10px;height:10px;background:#ddd;display:block}
.dots i.on{background:var(--red)}
.video{left:132px;top:584px;width:280px;height:220px;border:1px solid var(--line);padding:3px}
.video-screen{width:100%;height:100%;background:var(--dark);display:flex;align-items:center;justify-content:center}
.intro{left:442px;top:578px;width:628px}
.intro h1{font-size:20.5px;font-weight:400;color:#444;margin-bottom:10px}
.intro h1 em{font-style:normal;color:var(--red)}
.intro p{font-size:13.8px;line-height:20.4px;color:#444;margin-bottom:20px}
.footer-rule{left:132px;top:830px;width:936px;height:1px;background:var(--line)}
.footer-contact{left:132px;top:845px;font-size:13.5px;line-height:18px;color:var(--ink)}
.footer-contact h2{font-size:14.5px;font-weight:700;color:#111;margin-bottom:5px}
.follow{right:132px;top:842px;display:flex;align-items:center;gap:6px;font-size:14.5px;font-weight:700;color:#111}
.follow i{display:block;width:25px;height:25px;border-radius:50%;background:var(--social)}
.follow b{margin-right:8px}
.copyright{right:132px;top:870px;font-size:13.5px;color:var(--ink)}
</style>
</head>
<body>
<header>
  <div class="abs brand"><span class="brand-dot"></span><span class="brand-name">Lantern</span></div>
  <div class="abs contact-bar">
    <span><svg width="9" height="16" viewBox="0 0 9 16"><rect x="0.5" y="0.5" width="8" height="15" rx="1.5" fill="none" stroke="#888"/><rect x="2" y="2.5" width="5" height="9" fill="#888"/></svg>+1.888.555.0142</span>
    <span><svg width="15" height="11" viewBox="0 0 15 11"><rect x="0.5" y="0.5" width="14" height="10" fill="#999"/><path d="M0.5 0.5 L7.5 6 L14.5 0.5" fill="none" stroke="#fff"/></svg>info@lantern-outcomes.com</span>
  </div>
  <div class="abs lang"><span class="active">EN</span><span>FR</span><span class="signin">SIGN IN</span></div>
  <div class="abs search">Search...
    <svg width="18" height="18" viewBox="0 0 18 18"><circle cx="7.5" cy="7.5" r="5.5" fill="none" stroke="#333" stroke-width="2"/><line x1="11.5" y1="11.5" x2="16" y2="16" stroke="#333" stroke-width="2.2"/></svg>
  </div>
  <nav class="abs nav">
    <a class="home" href="#">Home</a>
    <a class="who" href="#">Who we are</a>
    <a class="cross" href="#">Cross the Lantern</a>
    <a class="perf" href="#">Performance Solutions</a>
    <a class="sustain" href="#">Sustain Solutions</a>
    <a class="join" href="#">Join Us</a>
  </nav>
</header>

<div class="abs hero" role="img" aria-label="Photo of a highway at night with light trails"></div>
<blockquote class="abs quote">“People often say that motivation doesn't last. Well,<br>neither does bathing.. &nbsp;that's why we recommend it daily.”<cite>- Dale Marrow</cite></blockquote>
<div class="abs dots"><i class="on"></i><i></i><i></i><i></i><i></i></div>

<div class="abs video">
  <div class="video-screen">
    <svg width="62" height="62" viewBox="0 0 62 62"><circle cx="31" cy="31" r="28" fill="none" stroke="#fff" stroke-width="3"/><path d="M24 18 L44 31 L24 44 Z" fill="#fff"/></svg>
  </div>
</div>

<section class="abs intro">
  <h1>Welcome to <em>Lantern Performance Group</em></h1>
  <p>Lantern Performance Group Inc. is the leading provider of profit generating and people development solutions. With the hands-on experience of best practices, the state-of-the-art technology and in-depth information we help companies increase their efficiencies and profits. Frank, honest, committed, valuable and rewarding are words that customers use to describe the quality services provided by Lantern Performance Group.</p>
  <p>Learn more about us, or find the right solutions for your specific business.We will be delighted to help you achieve better business results.</p>
</section>

<footer>
  <div class="abs footer-rule"></div>
  <div class="abs footer-contact">
    <h2>Contact Details :-</h2>
    Lantern Performance Group<br>
    2207 Harbour Rd, Elmsdale, NB E2K 3P8, Canada | &nbsp;Site Map
  </div>
  <div class="abs follow"><b>Follow Us :-</b><i></i><i></i><i></i></div>
  <div class="abs copyright">© 2013 lantern-outcomes.com. All rights reserved.</div>
</footer>
</body>
</html>
```